Pet sitting and Dog Walking Postcard distributed to new home owners in our target market

We need a two-sided postcard (or rack card, size can be anything rack card size or smaller) that is going in a folder that will be distributed each month to new homeowners in our target area. I would like the design to be similar to our brochure which will be uploaded here for you to see. It needs much less information than the brochure.
Should include services we offer; and our 4 systems: online registration, complimentary consultation, flexible scheduling, visits with reports and photos. Should also include our contact information (website, email, phone). Photos from the brochure can be used. Tagline from the cover of the brochure can be used. Call to action should be: Register on our website today to receive a free consultation and $20 off your first booking (when requesting a service, mention the promo code: welcome20).

```html
<!DOCTYPE html>
<html lang="en">
<head>
<meta charset="utf-8">
<title>Pawsome Valet Pet Care – Postcard</title>
<link href="https://fonts.googleapis.com/css2?family=Open+Sans:ital,wght@0,400;0,600;0,700;0,800;1,400&display=swap" rel="stylesheet">
<style>
  :root{
    --purple:#5d4a66;
    --green:#5cb848;
    --white:#ffffff;
    --ink:#4d4d4d;
    --page:#e9e7e4;
  }
  *{box-sizing:border-box;margin:0;padding:0}
  html,body{width:877px;height:1200px;overflow:hidden}
  body{background:var(--page);font-family:"Open Sans",Arial,sans-serif;color:var(--ink);position:relative}

  .card{position:absolute;left:30px;width:817px;height:520px;background:var(--white);overflow:hidden;box-shadow:0 4px 14px rgba(0,0,0,.18)}
  .card--front{top:40px}
  .card--back{top:640px}
  .card svg.shapes{position:absolute;inset:0;width:100%;height:100%}

  .brand{position:absolute;display:flex;align-items:center;gap:10px;color:var(--purple);font-weight:700;letter-spacing:.5px}
  .brand__dot{width:18px;height:18px;border-radius:50%;background:var(--purple)}
  .brand__name{font-size:20px;line-height:1.1;text-transform:uppercase}

  /* front */
  .front__brand{left:115px;top:68px}
  .front__copy{position:absolute;left:0;top:178px;width:400px;text-align:center;color:var(--white)}
  .front__title{font-size:25px;font-weight:700;line-height:1.2}
  .front__title span{display:block;color:var(--green)}
  .offer{margin:16px 14px 0 14px;border:2px dashed rgba(255,255,255,.8);border-radius:12px;padding:12px 8px}
  .offer__line{font-size:15px;line-height:1.35}
  .offer__line strong{color:var(--green);font-weight:700;text-transform:uppercase}
  .offer__note{font-size:9px;margin-top:4px}
  .front__serving{font-size:14px;line-height:1.35;margin-top:16px}
  .cta-pill{position:absolute;left:30px;top:455px;width:410px;height:30px;border-radius:15px;background:var(--green);color:var(--white);font-size:14px;font-weight:600;display:flex;align-items:center;justify-content:center;text-transform:uppercase;letter-spacing:.2px}
  .contact-row{position:absolute;left:24px;top:490px;display:flex;gap:30px;font-size:15px;font-weight:600;color:var(--ink)}
  .contact-row span{display:flex;align-items:center;gap:7px}
  .contact-row svg{width:16px;height:16px}

  /* back */
  .back__heading{position:absolute;left:26px;top:26px;font-size:22px;font-weight:700;color:var(--white)}
  .back__heading span{color:var(--green)}
  .back__intro{position:absolute;left:26px;top:70px;width:370px;font-size:10.5px;line-height:1.45;color:var(--white);font-weight:600}
  .steps{position:absolute;left:26px;top:140px;width:330px;list-style:none}
  .step{display:flex;gap:14px;margin-bottom:14px}
  .step__icon{flex:0 0 40px;width:40px;height:40px;border-radius:50%;background:var(--white);display:flex;align-items:center;justify-content:center}
  .step__icon svg{width:22px;height:22px}
  .step__title{font-size:14px;font-weight:700;color:var(--green);margin-bottom:3px}
  .step__text{font-size:10px;line-height:1.4;color:var(--white);font-style:italic}
  .back__brand{right:40px;top:60px}
  .why{position:absolute;left:510px;top:160px;width:307px;height:118px;background:var(--purple);color:var(--white);padding:20px 24px 0 40px}
  .why__title{font-size:22px;font-weight:700;text-align:right;margin-bottom:10px}
  .why__text{font-size:10px;line-height:1.4}
  .dog-photo{position:absolute;left:368px;top:290px;width:186px;height:172px;border-radius:86px 86px 10px 10px;background:radial-gradient(circle at 50% 40%,#faf6ef 0%,#e7dccb 55%,#c9b79e 100%)}
  .services{position:absolute;right:30px;top:300px;list-style:none;text-align:right}
  .services li{font-size:14px;font-weight:600;color:var(--purple);line-height:1.6;display:flex;align-items:center;justify-content:flex-end;gap:6px}
  .services svg{width:12px;height:12px}
  .phone-pill{position:absolute;right:22px;top:440px;width:205px;height:32px;border-radius:16px;background:var(--green);color:var(--white);font-size:17px;font-weight:700;display:flex;align-items:center;justify-content:center;gap:10px}
  .phone-pill svg{width:18px;height:18px}
  .back__footer{position:absolute;right:26px;top:492px;font-size:10px;color:var(--ink)}
</style>
</head>
<body>

<section class="card card--front">
  <svg class="shapes" viewBox="0 0 817 520" aria-hidden="true">
    <defs>
      <linearGradient id="frontPhoto" x1="0" y1="0" x2="1" y2="1">
        <stop offset="0" stop-color="#f3eee6"/>
        <stop offset=".5" stop-color="#d9c7ad"/>
        <stop offset="1" stop-color="#8a7563"/>
      </linearGradient>
    </defs>
    <rect x="0" y="160" width="480" height="290" fill="var(--purple)"/>
    <path d="M470 0 C 340 130, 345 390, 485 520 L817 520 L817 0 Z" fill="var(--green)"/>
    <path d="M482 0 C 355 130, 360 390, 500 520 L817 520 L817 0 Z" fill="var(--purple)"/>
    <path d="M500 0 C 375 130, 380 390, 520 520 L817 520 L817 0 Z" fill="url(#frontPhoto)" role="img" aria-label="Photo of a smiling woman on a sofa cuddling a dark brown dog"/>
    <path d="M640 0 C 740 20, 800 60, 817 90 L817 0 Z" fill="var(--green)"/>
    <path d="M720 0 C 770 15, 805 35, 817 55 L817 0 Z" fill="var(--purple)"/>
    <path d="M817 380 C 790 470, 720 510, 640 520 L817 520 Z" fill="var(--purple)"/>
    <path d="M817 430 C 795 490, 760 510, 720 520 L817 520 Z" fill="var(--green)"/>
    <circle cx="440" cy="250" r="46" fill="var(--white)"/>
    <circle cx="440" cy="250" r="41" fill="#a8876a" role="img" aria-label="Close-up photo of a dog resting under a striped blanket"/>
    <circle cx="440" cy="360" r="46" fill="var(--white)"/>
    <circle cx="440" cy="360" r="41" fill="#c7b7a3" role="img" aria-label="Photo of a hand stroking a tabby cat"/>
  </svg>

  <div class="brand front__brand">
    <span class="brand__dot"></span>
    <span class="brand__name">Pawsome Valet<br>Pet Care</span>
  </div>

  <div class="front__copy">
    <h1 class="front__title">Prioritize Yourself.<span>We'll Focus on Your Pets.</span></h1>
    <div class="offer">
      <p class="offer__line">Register on our website today<br><strong>to receive a free consultation</strong><br>and <strong style="text-transform:none;color:inherit">$20 off</strong> your first booking</p>
      <p class="offer__note">(when requesting a service, mention the promo code: welcome20)</p>
    </div>
    <p class="front__serving">Proudly serving Brookfield Heights &amp; surrounding<br>neighborhoods for over 15 years.</p>
  </div>

  <div class="cta-pill">For more information please contact us</div>

  <div class="contact-row">
    <span><svg viewBox="0 0 16 16"><circle cx="8" cy="8" r="7.5" fill="var(--ink)"/><path d="M5 4.5l1.5-.5 1 2-1 .8a5 5 0 0 0 2.7 2.7l.8-1 2 1-.5 1.5c-3.5.2-6.8-3-6.5-6.5z" fill="#fff"/></svg>555-014-WOOF</span>
    <span><svg viewBox="0 0 16 16"><circle cx="8" cy="8" r="7.5" fill="var(--ink)"/><circle cx="8" cy="8" r="4" fill="none" stroke="#fff" stroke-width="1.3"/><path d="M4 8h8M8 4v8" stroke="#fff" stroke-width="1"/></svg>www.pawsomevaletpets.example</span>
  </div>
</section>

<section class="card card--back">
  <svg class="shapes" viewBox="0 0 817 520" aria-hidden="true">
    <path d="M0 0 L455 0 C 585 150, 565 370, 455 520 L0 520 Z" fill="var(--purple)"/>
    <path d="M455 0 C 585 150, 565 370, 455 520" fill="none" stroke="var(--green)" stroke-width="8"/>
    <path d="M470 0 C 510 -5, 560 10, 600 40" fill="none" stroke="var(--green)" stroke-width="5"/>
    <rect x="440" y="478" width="377" height="42" fill="var(--white)"/>
  </svg>

  <h2 class="back__heading">Ready To Free Up <span>Your Time?</span></h2>
  <p class="back__intro">We are here to uncomplicate your life! Our systems and processes allow for seamless scheduling, service and billing. Give us a few minutes of your time and we will deliver it back to you tenfold!</p>

  <ul class="steps">
    <li class="step">
      <span class="step__icon"><svg viewBox="0 0 24 24"><rect x="3" y="5" width="18" height="12" rx="1.5" fill="none" stroke="var(--purple)" stroke-width="2"/><path d="M8 20h8M12 17v3" stroke="var(--purple)" stroke-width="2"/></svg></span>
      <div><h3 class="step__title">Online Registration</h3><p class="step__text">Click on the register link on our homepage to begin online registration or submit a request form if you would like more information first.</p></div>
    </li>
    <li class="step">
      <span class="step__icon"><svg viewBox="0 0 24 24"><path d="M4 5h16v10H10l-4 4v-4H4z" fill="none" stroke="var(--purple)" stroke-width="2" stroke-linejoin="round"/><circle cx="8.5" cy="10" r="1" fill="var(--purple)"/><circle cx="12" cy="10" r="1" fill="var(--purple)"/><circle cx="15.5" cy="10" r="1" fill="var(--purple)"/></svg></span>
      <div><h3 class="step__title">Complimentary Consultation</h3><p class="step__text">Request a consultation through our online portal. We'll reach out to you if you get stuck! Then we'll coordinate a meeting at your convenience.</p></div>
    </li>
    <li class="step">
      <span class="step__icon"><svg viewBox="0 0 24 24"><rect x="3" y="5" width="18" height="16" rx="1.5" fill="none" stroke="var(--purple)" stroke-width="2"/><path d="M3 10h18M8 3v4M16 3v4" stroke="var(--purple)" stroke-width="2"/></svg></span>
      <div><h3 class="step__title">Flexible Scheduling</h3><p class="step__text">Once we've met, we will be able to custom schedule your visits to fit your needs. You can always adjust your schedule through our portal app if your needs change.</p></div>
    </li>
    <li class="step">
      <span class="step__icon"><svg viewBox="0 0 24 24"><path d="M3 8h4l2-3h6l2 3h4v11H3z" fill="none" stroke="var(--purple)" stroke-width="2" stroke-linejoin="round"/><circle cx="12" cy="13" r="3.5" fill="none" stroke="var(--purple)" stroke-width="2"/></svg></span>
      <div><h3 class="step__title">Visits with Reports and Photos</h3><p class="step__text">Your pets will be cared for by our elite team of Pet Care Specialists. After each visit, you will receive an emailed report with photo.</p></div>
    </li>
  </ul>

  <div class="brand back__brand">
    <span class="brand__dot"></span>
    <span class="brand__name">Pawsome Valet<br>Pet Care</span>
  </div>

  <div class="why">
    <h2 class="why__title">Why Choose Us?</h2>
    <p class="why__text">We specialize in one-to-one personalized, quality pet care. We offer many services to cater to your needs. Whether you have dogs, cats, reptiles or rodents, we can help!</p>
  </div>

  <div class="dog-photo" role="img" aria-label="Photo of a white Labrador dog lying down wearing a blue collar"></div>

  <ul class="services">
    <li>Day Care &amp; Overnight Boarding<svg viewBox="0 0 14 14"><path d="M2 7l3.5 3.5L12 3" fill="none" stroke="var(--green)" stroke-width="2.4"/></svg></li>
    <li>Sleepovers<svg viewBox="0 0 14 14"><path d="M2 7l3.5 3.5L12 3" fill="none" stroke="var(--green)" stroke-width="2.4"/></svg></li>
    <li>Dog Walking<svg viewBox="0 0 14 14"><path d="M2 7l3.5 3.5L12 3" fill="none" stroke="var(--green)" stroke-width="2.4"/></svg></li>
    <li>Pet Sitting<svg viewBox="0 0 14 14"><path d="M2 7l3.5 3.5L12 3" fill="none" stroke="var(--green)" stroke-width="2.4"/></svg></li>
    <li>Cat Sitting/Small<svg viewBox="0 0 14 14"><path d="M2 7l3.5 3.5L12 3" fill="none" stroke="var(--green)" stroke-width="2.4"/></svg></li>
    <li>Pet Sitting<svg viewBox="0 0 14 14"><path d="M2 7l3.5 3.5L12 3" fill="none" stroke="var(--green)" stroke-width="2.4"/></svg></li>
  </ul>

  <div class="phone-pill">
    <svg viewBox="0 0 18 18"><circle cx="9" cy="9" r="8" fill="none" stroke="#fff" stroke-width="1.6"/><path d="M6 5l1.5-.5 1 2-1 .8a5 5 0 0 0 2.7 2.7l.8-1 2 1-.5 1.5C8.9 11.7 5.8 8.6 6 5z" fill="#fff"/></svg>
    555-014-WOOF
  </div>

  <p class="back__footer">info@pawsomevaletpets.example | www.pawsomevaletpets.example</p>
</section>

</body>
</html>
```